Uprising SaaS company needs an attractive business card design

We're an uprising SaaS company who's attempting to attack the rigid car (insurance) claims management market in Europe.
We want to our mighty base order management system, listen to our clients to connect the smart ideas to build something even mightier.
We primarily focus on helping our customers manage their customers' claims/orders and get them resolved as smoothly as possible.
We'd like the business card design to express technical innovation and the fact that we connect smart ideas, as our company slogan indicates.
Contact Information for Business Card
Name, position, website, email, mobile, business address
Font styles to use
Colors
Designer to choose colors to be used in the design.
Look and feel
Each slider illustrates characteristics of the customer's brand and the style your logo design should communicate.

```html
<!DOCTYPE html>
<html lang="en">
<head>
<meta charset="utf-8">
<title>Nexorva business card</title>
<link rel="stylesheet" href="https://fonts.googleapis.com/css2?family=Montserrat:wght@400;700&display=swap">
<style>
  :root {
    --page: #ececec;
    --card: #0a0a0a;
    --white: #ffffff;
    --accent: #7ccde3;
    --band-grey: #7b7b7b;
    --text-font: "Montserrat", sans-serif;
  }
  * { margin: 0; padding: 0; box-sizing: border-box; }
  html, body {
    width: 1200px; height: 728px; overflow: hidden;
    background: var(--page);
    font-family: var(--text-font);
  }
  .canvas { position: relative; width: 1200px; height: 728px; }
  .card {
    position: absolute; top: 210px;
    width: 511px; height: 307px;
    background: var(--card);
    overflow: hidden;
  }
  .card--front { left: 72px; }
  .card--back { left: 617px; }

  .card__band { position: absolute; left: 0; bottom: 0; width: 511px; height: 11px; }

  .brand-name {
    position: absolute;
    color: var(--white);
    font-weight: 400;
    letter-spacing: 0.5px;
    line-height: 1;
    white-space: nowrap;
  }
  .card--front .brand-name { left: 56px; top: 146px; font-size: 40px; }
  .card--back .brand-name { left: 0; width: 511px; text-align: center; top: 142px; font-size: 50px; }

  .divider { position: absolute; left: 277px; width: 1.5px; background: var(--white); }
  .divider--name { top: 99px; height: 38px; }
  .divider--contact { top: 158px; height: 50px; background: var(--accent); }

  .person { position: absolute; left: 287px; top: 97px; color: var(--white); }
  .person__name { font-size: 22.5px; font-weight: 700; letter-spacing: 0.3px; line-height: 1; }
  .person__name .surname { color: var(--accent); }
  .person__role { font-size: 13px; font-weight: 400; margin-top: 6px; line-height: 1; }

  .contacts { position: absolute; left: 287px; top: 155px; list-style: none; color: var(--white); }
  .contacts li {
    display: flex; align-items: center;
    font-size: 13.5px; line-height: 1; height: 20px;
  }
  .contacts svg { width: 12px; height: 12px; margin-right: 4px; flex: none; }
</style>
</head>
<body>
<main class="canvas">

  <section class="card card--front" aria-label="Business card front">
    <p class="brand-name">nexorva</p>

    <span class="divider divider--name"></span>
    <div class="person">
      <p class="person__name">MARA <span class="surname">DOYLE</span></p>
      <p class="person__role">CEO/Owner</p>
    </div>

    <span class="divider divider--contact"></span>
    <ul class="contacts">
      <li>
        <svg viewBox="0 0 12 12" aria-hidden="true"><circle cx="6" cy="6" r="6" fill="var(--accent)"/><path d="M4 3.2l1 1.4-.6.7c.4.8 1 1.4 1.8 1.8l.7-.6 1.4 1-.5.9c-2.4-.3-4.3-2.2-4.6-4.6z" fill="var(--card)"/></svg>
        (555) 014-2290
      </li>
      <li>
        <svg viewBox="0 0 12 12" aria-hidden="true"><circle cx="6" cy="6" r="6" fill="var(--accent)"/><rect x="3" y="4" width="6" height="4.2" fill="none" stroke="var(--card)" stroke-width="0.9"/><path d="M3 4l3 2.4L9 4" fill="none" stroke="var(--card)" stroke-width="0.9"/></svg>
        hello@nexorva.com
      </li>
      <li>
        <svg viewBox="0 0 12 12" aria-hidden="true"><circle cx="6" cy="6" r="6" fill="var(--accent)"/><g fill="none" stroke="var(--card)" stroke-width="0.7"><circle cx="6" cy="6" r="3.4"/><ellipse cx="6" cy="6" rx="1.4" ry="3.4"/><path d="M2.6 6h6.8M3.2 4.3h5.6M3.2 7.7h5.6"/></g></svg>
        www.nexorva.com
      </li>
    </ul>

    <svg class="card__band" viewBox="0 0 511 11" aria-hidden="true">
      <polygon points="0,0 351,0 360,11 0,11" fill="var(--band-grey)"/>
      <polygon points="351,0 356,0 365,11 360,11" fill="var(--card)"/>
      <polygon points="356,0 511,0 511,11 365,11" fill="var(--accent)"/>
    </svg>
  </section>

  <section class="card card--back" aria-label="Business card back">
    <p class="brand-name">nexorva</p>
    <svg class="card__band" viewBox="0 0 511 11" aria-hidden="true">
      <polygon points="0,0 351,0 360,11 0,11" fill="var(--band-grey)"/>
      <polygon points="351,0 356,0 365,11 360,11" fill="var(--card)"/>
      <polygon points="356,0 511,0 511,11 365,11" fill="var(--accent)"/>
    </svg>
  </section>

</main>
</body>
</html>
```